Social Media Graphics - Copperfield Loop

Create 6-7 individual social media graphics (square size) to encourage folks to join our online course, using either of the text below (only one set of text per graphic:

The Lantern Ridge Method
How to Create a 7-Figure Business From Scratch
Sign Up Today!

Or

The Lantern Ridge Method
Fast-track Your Way to a Multi-Million Business!
Sign Up Today!

For the color scheme of the graphics, use 1 or 2 colors in the color palette attached; or use any colors that look nice with their outfits; AVOID using red, white and blue altogether because it will look like an Independence Day (4th of July) graphic and we don’t want that; make sure the graphics appeal to both men and women

Make sure each graphic contains 1 of the 2 pics attached; and make sure one of the graphics is all TEXT only.

Target Market(s)

men and women looking to make more money

Industry/Entity Type

entrepreneurship

Requirements
Must have
• see the text document attached
Nice to have
• We are open to a nice color design; the color palette colors are not required, especially we don't want red, white and blue used together
Should not have
• AVOID using red, white and blue altogether because it will look like an Independence Day (4th of July) graphic and we dont want that

```html
<!DOCTYPE html>
<html lang="en">
<head>
<meta charset="utf-8">
<title>The Lantern Ridge Method – Social Graphics</title>
<link rel="stylesheet" href="https://fonts.googleapis.com/css2?family=Poppins:wght@400;600;700;800&family=Barlow+Condensed:wght@600&family=Roboto:wght@400&display=swap">
<style>
  :root{
    --canvas:#dedede;
    --teal-deep:#0e3b3a;
    --teal:#1d5c58;
    --plum:#4a1f3d;
    --plum-deep:#2e1226;
    --gold:#d6a84a;
    --gold-soft:#f0d58c;
    --gold-deep:#b5862c;
    --cream:#f7f0e2;
    --charcoal:#1b1b1d;
  }
  *{margin:0;padding:0;box-sizing:border-box}
  html,body{width:1189px;height:1200px;overflow:hidden;background:var(--canvas)}
  body{position:relative;font-family:"Poppins",sans-serif}

  .tile{position:absolute;width:349px;height:349px;overflow:hidden}
  .row-1{top:61px}
  .row-2{top:425px}
  .row-3{top:789px}

  .abs{position:absolute}
  .photo{position:absolute}
  .title{position:absolute;left:0;right:0;text-align:center;font-weight:800;font-size:34px;line-height:1.05;color:var(--cream);letter-spacing:-.5px}
  .tagline{position:absolute;left:0;right:0;text-align:center;font-family:"Roboto",sans-serif;font-size:12px;color:var(--cream)}
  .cta{position:absolute;display:flex;align-items:center;justify-content:center;border-radius:999px;font-weight:700;white-space:nowrap}
  .cta-small{width:120px;height:30px;font-size:11px}
  .cta-large{left:90px;width:170px;height:46px;font-size:15px}
  .cta-rule{position:absolute;height:2px;width:24px}
  .cta-rule.left{left:56px}
  .cta-rule.right{left:269px}

  /* 1 — teal, hosts photo */
  .t1{left:56px;background:var(--teal-deep)}
  .t1 .frame{left:22px;top:22px;width:305px;height:190px;border:2px solid var(--cream);border-bottom:none}
  .t1 .photo{left:0;top:30px;width:349px;height:319px;background:radial-gradient(ellipse at 50% 35%,#3b3430 0%,#1e2e2c 55%,rgba(14,59,58,0) 85%)}
  .t1 .title{top:190px}
  .t1 .tagline{top:270px}
  .t1 .cta{left:114px;top:298px;background:var(--gold);color:var(--charcoal)}

  /* 2 — plum, outlined title */
  .t2{left:420px;background:var(--plum)}
  .t2 .frame{left:20px;top:20px;width:309px;height:309px;border:2px solid var(--gold)}
  .t2 .photo{left:40px;top:30px;width:269px;height:319px;background:radial-gradient(ellipse at 50% 40%,#3a2b33 0%,#3a1a31 55%,rgba(74,31,61,0) 82%)}
  .t2 .title{top:100px;line-height:1.15}
  .t2 .outline{color:transparent;-webkit-text-stroke:1.1px var(--cream)}
  .t2 .tagline{top:196px;font-family:"Poppins",sans-serif;font-size:13px;line-height:18px;letter-spacing:.3px}
  .t2 .cta{left:114px;top:314px;background:var(--gold);color:var(--plum)}

  /* 3 — cream to gold, side pitch */
  .t3{left:784px;background:linear-gradient(180deg,var(--cream) 0%,var(--gold-soft) 40%,var(--gold) 75%,var(--gold-deep) 100%)}
  .t3 .heading{position:absolute;left:0;right:0;top:14px;text-align:center;font-weight:700;font-size:17px;color:var(--charcoal);letter-spacing:-.3px}
  .t3 .photo{left:0;top:50px;width:200px;height:299px;background:radial-gradient(ellipse at 50% 40%,#8c6a3a 0%,#5a4328 45%,rgba(181,134,44,0) 88%)}
  .t3 .pitch{position:absolute;right:12px;top:56px;text-align:right;font-weight:700;font-size:26px;line-height:31px;letter-spacing:-.5px}
  .t3 .pitch .dark{color:var(--charcoal)}
  .t3 .pitch .light{color:var(--plum)}
  .t3 .cta{left:217px;top:298px;background:var(--charcoal);color:var(--gold-soft)}

  /* 4 — charcoal, stacked pitch */
  .t4{left:238px;background:var(--charcoal)}
  .t4 .title{top:18px;font-size:28px;font-weight:700;color:var(--gold)}
  .t4 .rule{left:40px;top:84px;width:269px;height:2px;background:var(--gold)}
  .t4 .pitch{position:absolute;left:0;right:0;top:94px;text-align:center;font-family:"Barlow Condensed",sans-serif;font-weight:600;font-size:22px;line-height:23px;color:var(--cream)}
  .t4 .bars{left:0;top:195px;width:349px;height:40px}
  .t4 .photo{left:0;top:230px;width:349px;height:119px;background:radial-gradient(ellipse at 40% 60%,#5b4630 0%,#3a2e24 45%,#1b1b1d 100%)}

  /* 5 — text only */
  .t5{left:602px;background:radial-gradient(circle at 50% 45%,var(--gold-soft) 0%,#f6e6c0 30%,var(--cream) 62%)}
  .t5 .stripes{left:0;top:0;width:349px;height:349px}
  .t5 .frame{left:12px;top:12px;width:325px;height:210px;border:2px solid var(--teal);border-bottom:none}
  .t5 .title{top:100px;left:16px;right:auto;text-align:left;color:var(--teal-deep)}
  .t5 .tagline{top:186px;left:18px;right:auto;text-align:left;color:var(--teal-deep)}
  .t5 .cta{top:240px;background:var(--teal-deep);color:var(--cream)}
  .t5 .cta-rule{top:262px;background:var(--teal-deep)}

  /* 6 — teal with ghost word */
  .t6{left:238px;background:var(--teal-deep)}
  .t6 .ghost{position:absolute;left:0;top:12px;width:349px;text-align:center;font-weight:800;font-size:60px;color:#0a2e2d;letter-spacing:2px}
  .t6 .photo{left:0;top:30px;width:349px;height:319px;background:linear-gradient(100deg,#7a3a66 0%,#4a1f3d 32%,#1f2a2a 62%,rgba(14,59,58,.4) 100%)}
  .t6 .title{top:180px}
  .t6 .cta{top:272px;background:var(--cream);color:var(--teal-deep)}
  .t6 .cta-rule{top:294px;background:var(--cream)}

  /* 7 — gold with stripes */
  .t7{left:602px;background:linear-gradient(180deg,var(--gold) 0%,#cf9d3c 100%)}
  .t7 .stripes{left:0;top:0;width:349px;height:349px}
  .t7 .frame{left:12px;top:12px;width:325px;height:210px;border:2px solid var(--gold-soft);border-bottom:none}
  .t7 .photo{left:180px;top:12px;width:169px;height:90px;background:radial-gradient(ellipse at 60% 60%,#8a6530 0%,rgba(214,168,74,0) 75%)}
  .t7 .title{top:100px;left:16px;right:auto;text-align:left;color:var(--teal-deep)}
  .t7 .tagline{top:186px;left:18px;right:auto;text-align:left;color:var(--charcoal)}
  .t7 .cta{top:240px;background:var(--teal-deep);color:var(--gold-soft)}
  .t7 .cta-rule{top:262px;background:var(--teal-deep)}
</style>
</head>
<body>

<section class="tile row-1 t1">
  <div class="abs frame"></div>
  <div class="photo" role="img" aria-label="Photo of the two course hosts smiling, man in black turtleneck and woman in denim jacket"></div>
  <h2 class="title">THE LANTERN<br>RIDGE METHOD</h2>
  <p class="tagline">Fast-track Your Way to a Multi-Million Business!</p>
  <div class="cta cta-small">SIGN UP TODAY!</div>
</section>

<section class="tile row-1 t2">
  <div class="abs frame"></div>
  <div class="photo" role="img" aria-label="Photo of the two course hosts standing side by side, arms crossed"></div>
  <h2 class="title">TH<span class="outline">E LANT</span>ERN<br>R<span class="outline">IDGE METH</span>OD</h2>
  <p class="tagline">HOW TO CREATE A 7-FIGURE<br>BUSINESS FROM SCRATCH</p>
  <div class="cta cta-small">SIGN UP TODAY!</div>
</section>

<section class="tile row-1 t3">
  <h2 class="heading">THE LANTERN RIDGE METHOD</h2>
  <div class="photo" role="img" aria-label="Photo of the two course hosts, woman with arms crossed and man in black"></div>
  <p class="pitch"><span class="dark">How to<br>Create a<br>7-Figure</span><br><span class="light">Business<br>From<br>Scratch</span></p>
  <div class="cta cta-small">SIGN UP TODAY!</div>
</section>

<section class="tile row-2 t4">
  <h2 class="title">THE LANTERN<br>RIDGE METHOD</h2>
  <div class="abs rule"></div>
  <p class="pitch">FAST-TRACK<br>YOUR WAY TO A<br>MULTI-MILLION<br>BUSINESS!</p>
  <svg class="abs bars" viewBox="0 0 349 40" aria-hidden="true">
    <g stroke="var(--gold-deep)" stroke-width="2">
      <line x1="18" y1="0" x2="18" y2="40"/>
      <line x1="48" y1="8" x2="48" y2="40"/>
      <line x1="78" y1="16" x2="78" y2="40"/>
      <line x1="108" y1="22" x2="108" y2="40"/>
      <line x1="138" y1="26" x2="138" y2="40"/>
      <line x1="211" y1="26" x2="211" y2="40"/>
      <line x1="241" y1="22" x2="241" y2="40"/>
      <line x1="271" y1="16" x2="271" y2="40"/>
      <line x1="301" y1="8" x2="301" y2="40"/>
      <line x1="331" y1="0" x2="331" y2="40"/>
    </g>
  </svg>
  <div class="photo" role="img" aria-label="Photo of the two course hosts smiling side by side"></div>
</section>

<section class="tile row-2 t5">
  <svg class="abs stripes" viewBox="0 0 349 349" aria-hidden="true">
    <g stroke="#e6cf97" stroke-width="9" fill="none">
      <line x1="-10" y1="225" x2="360" y2="40"/>
      <line x1="-10" y1="251" x2="360" y2="66"/>
    </g>
  </svg>
  <div class="abs frame"></div>
  <h2 class="title">THE LANTERN<br>RIDGE METHOD</h2>
  <p class="tagline">Fast-track Your Way to a Multi-Million Business!</p>
  <span class="cta-rule left"></span>
  <div class="cta cta-large">SIGN UP TODAY!</div>
  <span class="cta-rule right"></span>
</section>

<section class="tile row-3 t6">
  <div class="ghost" aria-hidden="true">LANTERN</div>
  <div class="photo" role="img" aria-label="Photo of the two course hosts smiling"></div>
  <h2 class="title">THE LANTERN<br>RIDGE METHOD</h2>
  <span class="cta-rule left"></span>
  <div class="cta cta-large">SIGN UP TODAY!</div>
  <span class="cta-rule right"></span>
</section>

<section class="tile row-3 t7">
  <svg class="abs stripes" viewBox="0 0 349 349" aria-hidden="true">
    <g stroke="var(--gold-deep)" stroke-width="9" fill="none">
      <line x1="-10" y1="245" x2="360" y2="60"/>
      <line x1="-10" y1="271" x2="360" y2="86"/>
    </g>
  </svg>
  <div class="abs frame"></div>
  <div class="photo" role="img" aria-label="Small photo of the two course hosts"></div>
  <h2 class="title">THE LANTERN<br>RIDGE METHOD</h2>
  <p class="tagline">Fast-track Your Way to a Multi-Million Business!</p>
  <span class="cta-rule left"></span>
  <div class="cta cta-large">SIGN UP TODAY!</div>
  <span class="cta-rule right"></span>
</section>

</body>
</html>
```